We have developed a fully functional App called Corvalink. However, it requires a nicer GUI. You can see screenshots of our App on www.corvalink-example.com under "Tutorial". For those of you with Android, you can also install it. When you go to Corvalink-example.com, your phone will automatically redirect you to download. From there, you'll get a better idea of what our App looks like and how your design can make it way better. Please note we expect a design idea for most screens (there's about 8 screens) but do just one screen first and if you win, you can do the other 8 after.

Target Market(s)

People looking for dating / flirting

Industry/Entity Type

Android

Requirements
Must have
• sleek looking

```html
<!DOCTYPE html>
<html lang="en">
<head>
<meta charset="utf-8">
<title>Corvalink – Profile</title>
<link rel="stylesheet" href="https://fonts.googleapis.com/css2?family=Fira+Sans:wght@300;400;500&family=Roboto:wght@400;500&display=swap">
<style>
  :root{
    --page-bg:#2f7890;
    --status-bg:#151515;
    --status-blue:#3fb3e0;
    --header-top:#3d8aa3;
    --header-bottom:#1d6b85;
    --tab-top:#2b89a6;
    --tab-bottom:#1b6a86;
    --tab-divider:#14566d;
    --label:#1d5f78;
    --field-text:#8b6a86;
    --field-border:#d3bfd0;
    --field-bg:#fdfcfd;
    --accent:#b02a86;
    --accent-dark:#8e1f6c;
    --nav-top:#d65bb0;
    --nav-bottom:#b8338e;
    --nav-ink:#9a2377;
    --white:#ffffff;
  }
  *{box-sizing:border-box;margin:0;padding:0}
  html,body{width:1024px;height:1200px;overflow:hidden}
  body{background:var(--page-bg);font-family:"Fira Sans",sans-serif;position:relative}

  .screen{position:absolute;left:152px;top:0;width:720px;height:1200px;background:var(--white);overflow:hidden}

  .status-bar{position:absolute;left:0;top:0;width:100%;height:43px;background:var(--status-bg);
    display:flex;align-items:center;justify-content:flex-end;gap:12px;padding-right:16px}
  .status-time{font-family:"Roboto",sans-serif;font-size:29px;color:var(--status-blue);margin-left:6px}

  .app-header{position:absolute;left:0;top:43px;width:100%;height:181px;
    background:linear-gradient(160deg,var(--header-top),var(--header-bottom));
    display:flex;align-items:center;justify-content:center;gap:14px}
  .brand-dot{width:30px;height:30px;border-radius:50%;background:var(--accent)}
  .brand-name{font-size:52px;font-weight:500;color:var(--white);letter-spacing:1px}

  .tabs{position:absolute;left:0;top:224px;width:100%;height:94px;display:flex;
    background:linear-gradient(var(--tab-top),var(--tab-bottom))}
  .tab{flex:1;display:flex;align-items:center;justify-content:center;gap:8px;
    color:var(--white);font-family:"Roboto",sans-serif;font-weight:500;font-size:29px}
  .tab + .tab{border-left:1px solid var(--tab-divider)}
  .tab-pointer{position:absolute;left:183px;top:318px;width:0;height:0;
    border-left:34px solid transparent;border-right:34px solid transparent;border-top:26px solid var(--tab-bottom)}

  .field-label{position:absolute;left:45px;font-size:25px;color:var(--label)}
  .field{position:absolute;height:76px;border:2px solid var(--field-border);border-radius:5px;
    background:var(--field-bg);display:flex;align-items:center;padding-left:26px;
    font-size:25px;font-weight:300;color:var(--field-text);overflow:hidden;white-space:nowrap}
  .field .tick{position:absolute;right:22px;top:26px}
  .select-btn{position:absolute;right:-2px;top:-2px;bottom:-2px;width:43px;
    background:linear-gradient(var(--accent),var(--accent-dark));border-radius:0 5px 5px 0;
    display:flex;align-items:center;justify-content:center}

  .bottom-nav{position:absolute;left:0;top:1059px;width:100%;height:141px;display:flex;
    background:linear-gradient(var(--nav-top),var(--nav-bottom))}
  .nav-item{flex:1;display:flex;flex-direction:column;align-items:center;justify-content:center;gap:6px;
    color:var(--nav-ink);font-size:20px}
  .nav-item svg{height:52px}
  .nav-item + .nav-item{border-left:2px solid var(--nav-bottom)}
</style>
</head>
<body>
<main class="screen">
  <div class="status-bar">
    <svg width="26" height="26" viewBox="0 0 26 26" aria-hidden="true"><path d="M4 9h5l6-5v18l-6-5H4z" fill="#aaa"/><path d="M3 23 23 3" stroke="#aaa" stroke-width="2"/></svg>
    <svg width="30" height="28" viewBox="0 0 30 28" aria-hidden="true"><text x="0" y="11" font-size="11" fill="#aaa" font-family="Roboto,sans-serif">H</text><path d="M10 28 30 4v24z" fill="var(--status-blue)"/></svg>
    <svg width="18" height="28" viewBox="0 0 18 28" aria-hidden="true"><rect x="5" y="0" width="8" height="3" fill="var(--status-blue)"/><rect x="0" y="3" width="18" height="25" fill="var(--status-blue)"/></svg>
    <span class="status-time">13:37</span>
  </div>

  <header class="app-header">
    <span class="brand-dot"></span>
    <span class="brand-name">Corvalink</span>
  </header>

  <nav class="tabs">
    <div class="tab">
      <svg width="26" height="28" viewBox="0 0 26 28" aria-hidden="true"><circle cx="13" cy="8" r="6" fill="#5fa9c4"/><path d="M1 28c0-8 5-12 12-12s12 4 12 12z" fill="#5fa9c4"/></svg>
      Profile
    </div>
    <div class="tab">
      <svg width="22" height="28" viewBox="0 0 22 28" aria-hidden="true"><path d="M5 13V8a6 6 0 0 1 12 0v5" fill="none" stroke="#5fa9c4" stroke-width="3"/><rect x="1" y="12" width="20" height="16" rx="2" fill="#5fa9c4"/></svg>
      Security
    </div>
  </nav>
  <div class="tab-pointer"></div>

  <section class="profile-form">
    <label class="field-label" style="top:366px">Your Name</label>
    <div class="field" style="left:40px;top:417px;width:641px">Maya Rose
      <svg class="tick" width="22" height="18" viewBox="0 0 22 18" aria-hidden="true"><path d="M2 9l6 6L20 3" fill="none" stroke="var(--accent)" stroke-width="4"/></svg>
    </div>

    <label class="field-label" style="top:529px">Email</label>
    <div class="field" style="left:40px;top:579px;width:641px">lovelyrose27@corvamail.test
      <svg class="tick" width="22" height="18" viewBox="0 0 22 18" aria-hidden="true"><path d="M2 9l6 6L20 3" fill="none" stroke="var(--accent)" stroke-width="4"/></svg>
    </div>

    <label class="field-label" style="top:693px">Age</label>
    <label class="field-label" style="top:693px;left:216px">Height</label>
    <label class="field-label" style="top:693px;left:469px">Sex</label>

    <div class="field" style="left:40px;top:744px;width:133px">25
      <span class="select-btn"><svg width="16" height="26" viewBox="0 0 16 26" aria-hidden="true"><path d="M8 1 15 10H1zM8 25 1 16h14z" fill="#fff"/></svg></span>
    </div>
    <div class="field" style="left:212px;top:744px;width:218px">5’4”
      <span class="select-btn"><svg width="16" height="26" viewBox="0 0 16 26" aria-hidden="true"><path d="M8 1 15 10H1zM8 25 1 16h14z" fill="#fff"/></svg></span>
    </div>
    <div class="field" style="left:465px;top:744px;width:217px">F-Straight
      <span class="select-btn"><svg width="16" height="26" viewBox="0 0 16 26" aria-hidden="true"><path d="M8 1 15 10H1zM8 25 1 16h14z" fill="#fff"/></svg></span>
    </div>

    <label class="field-label" style="top:855px">Discovery</label>
    <div class="field" style="left:40px;top:906px;width:642px">World-Wide
      <span class="select-btn"><svg width="16" height="26" viewBox="0 0 16 26" aria-hidden="true"><path d="M8 1 15 10H1zM8 25 1 16h14z" fill="#fff"/></svg></span>
    </div>
  </section>

  <nav class="bottom-nav">
    <div class="nav-item">
      <svg width="54" height="52" viewBox="0 0 54 52" aria-hidden="true"><path d="M27 2 2 26h8v24h13V36h8v14h13V26h8z" fill="var(--nav-ink)"/></svg>
      Home
    </div>
    <div class="nav-item">
      <svg width="60" height="52" viewBox="0 -4 60 52" aria-hidden="true"><rect x="1" y="1" width="58" height="42" fill="var(--nav-ink)"/><path d="M2 2l28 22L58 2M2 42l20-20M58 42 38 22" fill="none" stroke="#c9479f" stroke-width="2"/></svg>
      Messages
    </div>
    <div class="nav-item">
      <svg width="46" height="52" viewBox="0 0 46 52" aria-hidden="true"><g fill="var(--nav-ink)"><rect x="3" y="2" width="6" height="48"/><rect x="0" y="30" width="12" height="8"/><rect x="20" y="2" width="6" height="48"/><rect x="17" y="12" width="12" height="8"/><rect x="37" y="2" width="6" height="48"/><rect x="34" y="22" width="12" height="8"/></g></svg>
      Settings
    </div>
  </nav>
</main>
</body>
</html>
```